flyer design for landscape group. i have enclosed my business card with logo

we are a local domestic and commercial landscaping group based in wokingham berkshire .we offer competitive landscaping solutions with a broad knowledge helping us solve problems in many fields such as new lawns, lawn care,tree care ,tree removal,hard and soft landscaping, decking, fencing ,garden or land clearance or just helping you with general maintanence. Being fully insured and certified for the job ,our excellent attention to detail has seen us recognised by local authorities and work for them on maintenance programmes performing in a safe and efficient manner

Target Market(s)

high end gardens commercial property

Industry/Entity Type

Landscaping

Requirements
Must have
• my logo . and some minimal sleek black and white design with small injections of colour
Should not have
• please do not include my full name or address only email and telephone

```html
<!DOCTYPE html>
<html lang="en">
<head>
<meta charset="utf-8">
<title>Fernwick – Landscaping Flyers</title>
<link href="https://fonts.googleapis.com/css2?family=Lato:wght@400;700;900&display=swap" rel="stylesheet">
<style>
  :root {
    --backdrop: #000000;
    --paper: #ffffff;
    --ink: #1a1a1a;
    --brand-brown: #3b2a20;
    --accent-orange: #f39200;
    --band-brown: #3a2a1e;
  }
  * { margin: 0; padding: 0; box-sizing: border-box; }
  html, body {
    width: 1200px; height: 844px; overflow: hidden;
    background: var(--backdrop);
    font-family: "Lato", Arial, sans-serif;
  }
  .sheet-row { position: relative; width: 1200px; height: 844px; }
  .flyer {
    position: absolute; top: 15px; width: 581px; height: 815px;
    background: var(--paper);
    text-align: center;
  }
  .flyer--leaves { left: 15px; }
  .flyer--garden { left: 607px; }

  .brand { position: absolute; top: 0; left: 0; right: 0; height: 182px; }
  .brand-dot {
    position: absolute; top: 44px; left: 50%; width: 40px; height: 40px;
    margin-left: -20px; border-radius: 50%; background: var(--accent-orange);
  }
  .brand-name {
    position: absolute; top: 114px; left: 0; right: 0;
    font-size: 32px; line-height: 40px; font-weight: 400; letter-spacing: 3px;
    color: var(--brand-brown);
  }

  .accent-band {
    position: absolute; top: 182px; left: 0; right: 0; height: 7px;
    background: var(--accent-orange);
  }
  .hero { position: absolute; top: 189px; left: 0; right: 0; height: 306px; }
  .hero--leaves {
    background: radial-gradient(circle at 60% 40%, #9a9a9a 0%, #6e6e6e 45%, #3c3c3c 100%);
  }
  .hero--garden {
    background: linear-gradient(180deg, #d8d8d8 0%, #a6a6a6 35%, #6f6f6f 70%, #4a4a4a 100%);
  }
  .hero-base {
    position: absolute; top: 495px; left: 0; right: 0; height: 8px;
    background: var(--band-brown);
  }
  .hero-headline {
    position: absolute; top: 329px; left: 0; right: 0;
    font-size: 26px; line-height: 32px; font-weight: 900; letter-spacing: 1.6px;
    color: var(--paper);
    text-shadow: 0 1px 4px rgba(0,0,0,0.7);
  }

  .services {
    position: absolute; top: 510px; left: 0; right: 0;
    font-size: 24px; line-height: 33px; color: var(--ink);
  }

  .contact { position: absolute; top: 674px; left: 0; right: 0; }
  .contact-call {
    font-size: 19px; line-height: 26px; font-weight: 700; color: var(--accent-orange);
  }
  .contact-email {
    margin-top: 12px;
    font-size: 16px; line-height: 22px; font-weight: 700; color: var(--ink);
  }
</style>
</head>
<body>
<main class="sheet-row">

  <article class="flyer flyer--leaves">
    <header class="brand">
      <span class="brand-dot"></span>
      <div class="brand-name">FERNWICK</div>
    </header>
    <div class="accent-band"></div>
    <div class="hero hero--leaves" role="img" aria-label="Black and white photograph of overlapping maple leaves and ferns"></div>
    <h2 class="hero-headline">CERTIFIED LANDSCAPING SOLUTION</h2>
    <div class="hero-base"></div>
    <p class="services">
      new lawns • lawn care • tree care • tree removal<br>
      hard and soft landscaping • decking • fencing<br>
      garden or land clearance • general maintenance
    </p>
    <footer class="contact">
      <p class="contact-call">CALL US NOW: 0770 000 4821</p>
      <p class="contact-email">hello@fernwickgardens.co.uk</p>
    </footer>
  </article>

  <article class="flyer flyer--garden">
    <header class="brand">
      <span class="brand-dot"></span>
      <div class="brand-name">FERNWICK</div>
    </header>
    <div class="accent-band"></div>
    <div class="hero hero--garden" role="img" aria-label="Black and white photograph of a paved courtyard garden with benches, planters and ivy"></div>
    <h2 class="hero-headline">EXCELLENT ATTENTION TO DETAIL</h2>
    <div class="hero-base"></div>
    <p class="services">
      new lawns • lawn care • tree care • tree removal<br>
      hard and soft landscaping • decking • fencing<br>
      garden or land clearance • general maintenance
    </p>
    <footer class="contact">
      <p class="contact-call">CALL US NOW: 0770 000 4821</p>
      <p class="contact-email">hello@fernwickgardens.co.uk</p>
    </footer>
  </article>

</main>
</body>
</html>
```